TAVRO Capital Group LLC a High Risk Big Rewards company for Rich Young Entrepreneurs

We would like a very modern, powerful in the eyes of our customers, modern, minimalist feel, financial gain. this business card is for young Rich entrepreneurs who want to invest money into High Risk, Big Rewards Businesses. The card Should sell the business!! let your creativity go Wild! I pick most of the designers for this project because of your BOLD Designs, I would like this card to be Bold, Modern, Minimalist, use as many effects in your graphic Artist Mind, Do not let the Financial sound of this business to make you think Conservative that's the last thing we are! if you have a lot of money and you want to play a risky market call US
Updates

Project Deadline Extended
Reason: have not received, enough designs to choose 1st and second place, sure I have received over 100 designs but it seems most designers are submitting every card they have ever made before and calling it mine, please we are looking for fresh ideas please!

Target Market(s)

Private Risky Investors

Industry/Entity Type

Financial

Contact Information for Business Card

powerful in the eyes of our customers,modern, minimalist feel

Font styles to use
Other font styles liked:
• Modern feeling fonts

Requirements
Must have
• The Company Name is TAVRO Capital Group LLC and it must be on the CARD
• My Name, title, Cell , email
• Delvin Ashcroft G.E.D.
• Managing Member
• 555.038.6195
• delvin@tavrocapitalgroup.example
Nice to have
• try a black thick plastic card with round corners with Delvin Ashcroft GED (make sure GED is smaller than name) just on one side of the card, and my phone number with out the icons and email on the other side, this card should look like a exclusive credit card or exclusive VIP card, something you would never loose

```html
<!DOCTYPE html>
<html lang="en">
<head>
<meta charset="utf-8">
<title>TAVRO Capital Group LLC – Business Card</title>
<link rel="stylesheet" href="https://fonts.googleapis.com/css2?family=Open+Sans:wght@600;700;800&display=swap">
<style>
  :root {
    --page-bg: #2a2a2a;
    --card-dark: #141414;
    --card-mid: #262626;
    --card-edge: #303030;
    --gold: #e8c10c;
    --gold-deep: #b38f00;
    --gold-light: #fbe46a;
  }
  html, body {
    margin: 0;
    padding: 0;
    width: 1200px;
    height: 660px;
    overflow: hidden;
    background: var(--page-bg);
  }
  .canvas {
    position: relative;
    width: 1200px;
    height: 660px;
    display: flex;
    align-items: center;
    justify-content: center;
    gap: 40px;
    font-family: "Open Sans", Arial, sans-serif;
  }
  .card {
    position: relative;
    width: 540px;
    height: 309px;
    border-radius: 4px;
    overflow: hidden;
    box-shadow: 0 14px 30px rgba(0, 0, 0, 0.55);
    display: flex;
    flex-direction: column;
    align-items: center;
    justify-content: center;
    text-align: center;
  }
  .card-texture {
    position: absolute;
    inset: 0;
    background:
      radial-gradient(ellipse at 30% 25%, var(--card-edge) 0%, transparent 55%),
      radial-gradient(ellipse at 75% 80%, var(--card-mid) 0%, transparent 60%),
      linear-gradient(135deg, var(--card-mid) 0%, var(--card-dark) 100%);
  }
  .gold-text {
    position: relative;
    margin: 0;
    color: var(--gold);
    text-shadow: 0 1px 0 var(--gold-deep), 0 -1px 0 var(--gold-light), 0 2px 3px rgba(0, 0, 0, 0.6);
    text-transform: uppercase;
  }
  .company-name {
    font-size: 27px;
    font-weight: 800;
    letter-spacing: 1px;
  }
  .holder-name {
    font-size: 27px;
    font-weight: 800;
    letter-spacing: 1px;
  }
  .holder-name .credential {
    font-size: 21px;
  }
  .holder-title {
    margin-top: 10px;
    font-size: 22px;
    font-weight: 700;
    text-transform: none;
  }
  .contact-phone {
    margin-top: 12px;
    font-size: 17px;
    font-weight: 700;
    letter-spacing: 1px;
  }
  .contact-email {
    margin-top: 22px;
    font-size: 12px;
    font-weight: 700;
    letter-spacing: 0.5px;
  }
  .contact-email .address {
    text-decoration: underline;
  }
</style>
</head>
<body>
  <main class="canvas">
    <section class="card card-front">
      <div class="card-texture" role="img" aria-label="Dark low-poly faceted background texture"></div>
      <h1 class="gold-text company-name">TAVRO Capital Group LLC</h1>
    </section>

    <section class="card card-back">
      <div class="card-texture" role="img" aria-label="Dark low-poly faceted background texture"></div>
      <h2 class="gold-text holder-name">Delvin Ashcroft <span class="credential">G.E.D</span></h2>
      <p class="gold-text holder-title">Managing Member</p>
      <p class="gold-text contact-phone">Phone : 555.038.6195</p>
      <p class="gold-text contact-email">Email : <span class="address">delvin@tavrocapitalgroup.example</span></p>
    </section>
  </main>
</body>
</html>
```